German tourism publishing house needs for international wellness hotel guide

We are planning as a print catalog. For this hotel directory we need a meaningful and appealing cover. The contents, a wide offer of wellness hotels should be recognizable at first sight. The title should make you want to go on a wellness holiday. The target group of the book are customers. We are looking forward to your next visit! The title "Wellness Hotels" should be larger on the cover written. The "Bravora logo" should be smaller on the cover. Please integrate the Internet address www.bravora-example.de small on the cover

Industry/Entity Type

Tourism

Font styles to use
Serif
Sans Serif

Colors
0355a3
ffffff
85acd3

Requirements
Must have
• We are looking forward to your next visit! The title "Wellness Hotels" should be larger on the cover written. The "Bravora logo" should be smaller on the cover.
Nice to have
• Please integrate the Internet address www.bravora-example.de small on the cover

```html
<!DOCTYPE html>
<html lang="en">
<head>
<meta charset="utf-8">
<title>Bravora Wellness Hotel Guide – Cover</title>
<link rel="stylesheet" href="https://fonts.googleapis.com/css2?family=Bungee&family=Open+Sans:wght@400;600&display=swap">
<style>
  :root {
    --stage: #000000;
    --brand-blue: #0355a3;
    --title-blue: #1f8fd6;
    --sky: #00aee0;
    --soft-blue: #85acd3;
    --white: #ffffff;
    --paper: #f4f7fb;
    --ring: #3fb7d8;
    --hub-ring: #9fd9ea;
  }
  * { margin: 0; padding: 0; box-sizing: border-box; }
  html, body { width: 1200px; height: 847px; overflow: hidden; background: var(--stage); }
  body { position: relative; font-family: "Open Sans", Arial, sans-serif; }

  .spread-label {
    position: absolute; top: 66px; width: 200px; text-align: center;
    color: var(--white); font-size: 19px; line-height: 24px;
  }
  .spread-label--back { left: 256px; }
  .spread-label--front { left: 768px; }

  .cover { position: absolute; top: 108px; width: 510px; height: 666px; overflow: hidden; }
  .cover--back { left: 100px; background: var(--sky); }
  .cover--front { left: 612px; background: linear-gradient(180deg, var(--white), var(--paper)); }

  .web-address {
    position: absolute; top: 34px; left: 0; width: 100%; text-align: center;
    color: var(--white); font-size: 13px; line-height: 18px; letter-spacing: 1.5px;
  }

  .photo {
    position: absolute; border-radius: 50%;
    border: 2px solid var(--white);
    box-shadow: 0 2px 5px rgba(0,0,0,.3);
  }
  .photo--small { width: 106px; height: 106px; }

  .hub {
    position: absolute; left: 158px; top: 230px; width: 196px; height: 196px;
    border-radius: 50%; background: var(--white);
    box-shadow: 0 0 0 8px var(--hub-ring);
  }
  .cover-title { position: absolute; overflow: visible; }
  .cover-title text { font-family: "Bungee", Impact, sans-serif; fill: var(--title-blue); stroke: var(--brand-blue); }

  .wordmark {
    position: absolute; color: var(--brand-blue);
    font-family: "Open Sans", Arial, sans-serif; font-weight: 600; font-size: 40px;
    line-height: 1;
  }
  .wordmark--back { left: 0; width: 100%; text-align: center; top: 594px; }
  .wordmark--front { left: 36px; top: 604px; }

  .ring {
    position: absolute; border-radius: 50%; border: 1.5px solid var(--ring);
    background: var(--white);
  }
  .ring .photo { border: none; box-shadow: none; }

  .plant-art {
    position: absolute; left: 345px; top: 348px; width: 160px; height: 318px;
    background: linear-gradient(160deg, rgba(133,172,211,0) 10%, rgba(133,172,211,.45) 50%, rgba(133,172,211,.25) 90%);
    border-radius: 60% 40% 30% 50%;
  }
  .page-url {
    position: absolute; left: 674px; top: 824px; color: var(--brand-blue);
    font-size: 16px; line-height: 20px;
  }
</style>
</head>
<body>
  <div class="spread-label spread-label--back">Back Cover</div>
  <div class="spread-label spread-label--front">Front Cover</div>

  <section class="cover cover--back">
    <p class="web-address">www.bravora-example.de</p>

    <div class="photo photo--small" style="left:89px;top:169px;background:linear-gradient(135deg,#f0b27a,#b8623a 55%,#7a3a22);" role="img" aria-label="Photo: warm lit relaxation room with birch trunks"></div>
    <div class="photo photo--small" style="left:202px;top:125px;background:linear-gradient(160deg,#b88a55,#e8dccb 50%,#f4f1ec);" role="img" aria-label="Photo: woman in bathrobe resting"></div>
    <div class="photo photo--small" style="left:315px;top:169px;background:linear-gradient(160deg,#f7b640,#f3d7a6 55%,#c8352a);" role="img" aria-label="Photo: woman relaxing on a lounger"></div>
    <div class="photo photo--small" style="left:41px;top:281px;background:linear-gradient(180deg,#e6b35a,#c9a070 55%,#3a3a48);" role="img" aria-label="Photo: two women doing yoga"></div>
    <div class="photo photo--small" style="left:361px;top:281px;background:linear-gradient(180deg,#b07a45,#f0e8de 55%,#a8763e);" role="img" aria-label="Photo: couple in a wooden sauna"></div>
    <div class="photo photo--small" style="left:89px;top:394px;background:linear-gradient(180deg,#5a3a2c,#3d7ec0 50%,#d8204a);" role="img" aria-label="Photo: massage treatment with singing bowl"></div>
    <div class="photo photo--small" style="left:202px;top:439px;background:linear-gradient(180deg,#d8b47a,#a0805a 55%,#eeeae4);" role="img" aria-label="Photo: man relaxing on a lounger"></div>
    <div class="photo photo--small" style="left:315px;top:394px;background:linear-gradient(120deg,#e89a48,#8a5a34 55%,#c9c2b8);" role="img" aria-label="Photo: sauna area with salt wall"></div>

    <div class="hub"></div>
    <svg class="cover-title" style="left:182px;top:284px" width="146" height="82" viewBox="0 0 146 82">
      <text x="0" y="30" textLength="144" lengthAdjust="spacingAndGlyphs" font-size="30" stroke-width=".6">WELLNESS</text>
      <text x="0" y="78" textLength="146" lengthAdjust="spacingAndGlyphs" font-size="42" stroke-width=".6">HOTELS</text>
    </svg>

    <div class="wordmark wordmark--back">Bravora</div>
  </section>

  <section class="cover cover--front">
    <svg class="cover-title" style="left:34px;top:28px" width="344" height="160" viewBox="0 0 344 160">
      <text x="0" y="60" textLength="332" lengthAdjust="spacingAndGlyphs" font-size="68" stroke-width="1">WELLNESS</text>
      <text x="0" y="158" textLength="340" lengthAdjust="spacingAndGlyphs" font-size="100" stroke-width="1">HOTELS</text>
    </svg>

    <svg style="position:absolute;left:0;top:0" width="510" height="666" viewBox="0 0 510 666">
      <path d="M0 212 C40 200 60 210 100 270" fill="none" stroke="var(--sky)" stroke-width="6" stroke-linecap="round"/>
      <path d="M0 212 C40 204 64 214 100 272" fill="none" stroke="#9fd9ea" stroke-width="2"/>
      <path d="M280 284 C340 260 380 240 460 218" fill="none" stroke="#5cb8e6" stroke-width="5" stroke-linecap="round"/>
      <path d="M460 230 C490 270 500 320 505 360" fill="none" stroke="var(--sky)" stroke-width="3" stroke-linecap="round"/>
    </svg>

    <div class="plant-art" role="img" aria-label="Illustration: stylised blue plant with leaves"></div>

    <div class="ring" style="left:24px;top:257px;width:272px;height:272px;">
      <div class="photo" style="left:16px;top:13px;width:242px;height:244px;background:linear-gradient(180deg,#b9d2e6 0%,#8fa8b8 18%,#5f8a3e 38%,#7a6a5c 62%,#5a4a40 100%);" role="img" aria-label="Photo: garden terrace with lounge furniture by a pond"></div>
    </div>
    <div class="ring" style="left:316px;top:185px;width:172px;height:172px;">
      <div class="photo" style="left:10px;top:3px;width:154px;height:154px;background:linear-gradient(180deg,#4a3a2a 0%,#b58860 40%,#e2c4a4 70%,#7a5a40 100%);" role="img" aria-label="Photo: couple relaxing in an indoor pool"></div>
    </div>

    <div class="wordmark wordmark--front">Bravora</div>
  </section>

  <div class="page-url">www.bravora-example.de</div>
</body>
</html>
```